Website Design for Venture Capital firm

Create website for venture capital firm. Website Instructions
Use https://www.korventholdings.com/ as a reference website.
Use images of Downtown Austin, Texas.
Use images of business executives in business suits, pictures of money coins stacked like a graph cart.
Use images of downtown high rise buildings.
Use the same image of the Big Ben Clock that appears on Korvent Holdings website.
Use images associated with Venture Technology Incubator.
Use images associated with Venture Angel Investor.
Create Section Heads for the menu bar for each of the sections below.
Use the Orchid Slate Advisors HEADER to guide your style
Target Market(s)
Venture Capital Investors
Number of Pages Required
1 page
Look and feel
Each slider illustrates characteristics of the customer's brand and the style your logo design should communicate.

```html
<!DOCTYPE html>
<html lang="en">
<head>
<meta charset="utf-8">
<title>Orchid Slate Advisors</title>
<link href="https://fonts.googleapis.com/css2?family=Josefin+Sans:wght@300;400;600;700&display=swap" rel="stylesheet">
<style>
:root{
  --green:#123d26;
  --gold:#e8b834;
  --ink:#1d1d1d;
  --white:#ffffff;
  --rule:#d9d9d9;
}
*{margin:0;padding:0;box-sizing:border-box}
html,body{width:1200px;height:3117px;overflow:hidden;background:var(--white)}
body{position:relative;font-family:"Josefin Sans",sans-serif;color:var(--ink)}
.abs{position:absolute}
.brand{font-family:"Josefin Sans",sans-serif;font-weight:600;color:var(--green);letter-spacing:2px;line-height:1.1;text-transform:uppercase}
.nav a{position:absolute;font-size:18px;color:#333;text-decoration:none;font-weight:400}
.nav a.current{color:var(--green);text-decoration:underline;text-underline-offset:4px}
.btn{position:absolute;background:var(--gold);color:var(--ink);font-size:18px;display:flex;align-items:center;justify-content:center;text-decoration:none;padding-top:3px}
.band{position:absolute;left:0;width:1200px}
.band-title{position:absolute;color:var(--white);font-weight:600;text-transform:uppercase;line-height:1.2;text-shadow:0 2px 6px rgba(0,0,0,.4)}
.heading{position:absolute;font-weight:600;font-size:38px;line-height:44px;text-transform:uppercase;color:var(--green)}
.heading span{color:var(--gold);display:block}
.copy{position:absolute;font-size:17px;line-height:28px}
.copy p+p{margin-top:6px}
.benefit-icon{position:absolute;left:639px;width:69px;height:69px;border-radius:50%;background:var(--gold)}
.benefit-text{position:absolute;left:640px;width:420px;font-size:15.5px;line-height:24px;color:#333}
</style>
</head>
<body>

<header>
  <div class="brand abs" style="left:102px;top:36px;font-size:26px;width:260px">Orchid Slate<br>Advisors</div>
  <nav class="nav">
    <a class="current" style="left:452px;top:42px">Overview</a>
    <a style="left:563px;top:42px">Approach</a>
    <a style="left:674px;top:42px">Citizenship</a>
    <a style="left:794px;top:42px">Team</a>
    <a style="left:871px;top:42px">Contact</a>
  </nav>
  <a class="btn" style="left:957px;top:36px;width:139px;height:40px">Investor Login</a>
</header>

<section class="band" style="top:100px;height:600px;background:linear-gradient(180deg,#1c2f52 0%,#2e3e5c 45%,#8a6a3e 62%,#2b3140 78%,#1a2230 100%)" role="img" aria-label="Downtown Austin skyline at dusk over the river with a bridge">
  <div class="abs" style="left:0;top:170px;width:1200px;text-align:center;color:#fff;font-size:24px;font-weight:600;text-shadow:0 2px 6px rgba(0,0,0,.4)">WELCOME TO ORCHID SLATE ADVISORS</div>
  <div class="band-title" style="left:0;top:208px;width:1200px;text-align:center;font-size:48px;line-height:56px">Empowering businesses to<br>thrive in changing markets</div>
  <a class="btn" style="left:542px;top:334px;width:131px;height:39px">Get Started</a>
</section>

<section>
  <div class="abs" style="left:104px;top:780px;width:455px;height:393px;background:linear-gradient(135deg,#e6e9ec,#b9bec4 55%,#6f7378)" role="img" aria-label="Three business executives in suits reviewing work on a laptop"></div>
  <h2 class="heading" style="left:639px;top:800px;width:480px">About Orchid Slate<span>Advisors</span></h2>
  <div class="copy" style="left:639px;top:892px;width:455px">
    <p>Orchid Venture Advisors is a Startup Technology Incubator, Seed-Stage Venture Investor and Late-Stage Co-Investor in companies seeking to compete in the consumer services and business services sectors.</p>
    <p>Similar to other leading technology incubators, Orchid Venture Advisors provides a combination of seed capital investment,</p>
  </div>
  <a class="btn" style="left:640px;top:1101px;width:131px;height:40px">Read more</a>
</section>

<section class="band" style="top:1252px;height:480px;background:linear-gradient(160deg,#1a2a4a 0%,#2f5a93 45%,#5b8bc8 70%,#1d3260 100%)" role="img" aria-label="Glass high-rise towers viewed from below against a blue sky">
  <div class="band-title" style="left:103px;top:155px;font-size:42px;line-height:50px">Incubator &amp; seed stage<br>investment model</div>
  <a class="btn" style="left:103px;top:282px;width:131px;height:39px">Read more</a>
</section>

<section>
  <h2 class="heading" style="left:104px;top:1800px;width:500px">Benefits of investing<span>in venture</span></h2>
  <div class="copy" style="left:104px;top:1900px;width:470px">Venture capital allows investors to diversify their portfolios beyond traditional asset classes (stocks, bonds, real estate).</div>

  <svg class="benefit-icon" style="top:1817px" viewBox="0 0 69 69"><g fill="none" stroke="#1d1d1d" stroke-width="1.6"><path d="M20 44h30M24 44v-6M31 44v-10M38 44v-13M45 44v-17"/><path d="M22 34l9-8 7 4 11-10"/></g></svg>
  <div class="benefit-text" style="top:1906px">Investing in venture capital deals can lead to significant returns, especially if the company grows rapidly or goes public.</div>

  <svg class="benefit-icon" style="top:2003px" viewBox="0 0 69 69"><g fill="none" stroke="#1d1d1d" stroke-width="1.6"><path d="M34.5 18c6 4 7 14 4 22h-8c-3-8-2-18 4-22z"/><circle cx="34.5" cy="30" r="3"/><path d="M31 44h7M32 48h5M18 34h5M46 34h5"/></g></svg>
  <div class="benefit-text" style="top:2092px">Early-stage investments in successful startups often yield returns much higher than traditional investments like stocks or bonds.</div>

  <svg class="benefit-icon" style="top:2185px" viewBox="0 0 69 69"><g fill="none" stroke="#1d1d1d" stroke-width="1.6"><path d="M18 48h33"/><rect x="21" y="40" width="5" height="8"/><rect x="29" y="35" width="5" height="13"/><rect x="37" y="30" width="5" height="18"/><rect x="45" y="24" width="5" height="24"/><path d="M20 34l12-9 6 3 10-8M44 20h4v4"/></g></svg>
  <div class="benefit-text" style="top:2275px">Venture capital gives investors access to high-growth startups, some of which may become "Unicorns" (companies valued at over $1 billion).</div>
</section>

<section class="band" style="top:2431px;height:478px;background:linear-gradient(180deg,#1a1f33 0%,#2c2a45 40%,#6a3a36 62%,#3a2530 78%,#141722 100%)" role="img" aria-label="Big Ben clock tower and Westminster at dusk reflected on the river">
  <div class="band-title" style="left:567px;top:146px;font-size:42px;line-height:50px">Risks of investing as an<br>angel venture investor</div>
  <div class="abs" style="left:567px;top:255px;color:#fff;font-size:14.5px">The majority of startups fail, often within the first few years of operation.</div>
  <a class="btn" style="left:567px;top:289px;width:131px;height:39px">Read more</a>
</section>

<footer>
  <div class="brand abs" style="left:104px;top:2972px;font-size:30px;width:320px">Orchid Slate<br>Advisors</div>
  <nav class="nav">
    <a class="current" style="left:560px;top:2980px">Overview</a>
    <a style="left:671px;top:2980px">Approach</a>
    <a style="left:782px;top:2980px">Citizenship</a>
    <a style="left:901px;top:2980px">Team</a>
    <a style="left:979px;top:2980px">Contact</a>
  </nav>
  <div class="abs" style="left:104px;top:3052px;width:992px;height:1px;background:var(--rule)"></div>
  <div class="abs" style="left:0;top:3078px;width:1200px;text-align:center;font-size:13px;color:#333">© 2024 Orchid Slate Advisors, LLC.</div>
</footer>

</body>
</html>
```